Business card design needed

It's a new business in town.Something so the name stands out.I need a logo for the B.R.W
I may all so use the design as a sign on a building

Contact Information for Business Card

B.R.W
Brindlewood Auto Detailing
42 Fenwarra Crs
Brindlewood Vic 3799
Ph:(03)59284736
Mob:0417362958

```html
<!DOCTYPE html>
<html lang="en">
<head>
<meta charset="utf-8">
<title>B.R.W – Brindlewood Auto Detailing business cards</title>
<link rel="stylesheet" href="https://fonts.googleapis.com/css2?family=Fira+Sans:ital,wght@0,300;0,400;0,600;0,700;1,700&display=swap">
<style>
  :root {
    --backdrop: #e6e1d8;
    --red-base: #8e242c;
    --red-light: #a12a33;
    --red-dark: #7c1f27;
    --slate-base: #2f3942;
    --slate-light: #3d4953;
    --slate-dark: #252e35;
    --cream: #f1ede0;
    --disc: #e0ddcc;
    --accent-red: #d4202a;
    --accent-blue: #2fa9e1;
    --white: #ffffff;
  }
  * { box-sizing: border-box; margin: 0; padding: 0; }
  html, body { width: 1200px; height: 900px; overflow: hidden; }
  body {
    background: var(--backdrop);
    font-family: "Fira Sans", sans-serif;
    display: grid;
    grid-template-columns: 540px 540px;
    grid-template-rows: 320px 320px;
    gap: 30px;
    padding: 115px 45px;
  }
  .card {
    position: relative;
    width: 540px;
    height: 320px;
    overflow: hidden;
    box-shadow: 0 6px 14px rgba(0,0,0,.25);
  }
  .card-front--red {
    background:
      linear-gradient(90deg,
        var(--red-dark) 0 4%, var(--red-light) 4% 10%, var(--red-dark) 10% 16%,
        var(--red-light) 16% 22%, var(--red-dark) 22% 28%, var(--red-light) 28% 34%,
        var(--red-dark) 34% 40%, var(--red-light) 40% 46%, var(--red-dark) 46% 52%,
        var(--red-base) 52% 100%);
  }
  .card-front--slate {
    background:
      linear-gradient(90deg,
        var(--slate-dark) 0 4%, var(--slate-light) 4% 10%, var(--slate-dark) 10% 16%,
        var(--slate-light) 16% 22%, var(--slate-dark) 22% 28%, var(--slate-light) 28% 34%,
        var(--slate-dark) 34% 40%, var(--slate-light) 40% 46%, var(--slate-dark) 46% 52%,
        var(--slate-base) 52% 100%);
  }
  .front-mark {
    position: absolute;
    left: 78px; top: 100px;
    width: 160px; height: 136px;
    border-radius: 50%;
    background: var(--disc);
    display: flex; align-items: center; justify-content: center;
    font-weight: 700;
    font-size: 34px;
  }
  .card-front--red .front-mark { color: var(--accent-red); }
  .card-front--slate .front-mark { color: var(--accent-blue); }
  .front-details {
    position: absolute;
    left: 312px; top: 122px;
    color: var(--white);
  }
  .business-name {
    font-weight: 700;
    font-style: italic;
    font-size: 36px;
    line-height: 1;
    letter-spacing: 1px;
  }
  .business-tagline {
    font-weight: 300;
    font-size: 14px;
    margin-top: 4px;
  }
  .business-contact {
    font-style: normal;
    font-weight: 600;
    font-size: 13px;
    line-height: 18px;
    margin-top: 40px;
    letter-spacing: .3px;
  }
  .card-back {
    background: var(--cream);
  }
  .back-disc {
    position: absolute;
    left: 50%; top: 50%;
    width: 440px; height: 440px;
    margin: -220px 0 0 -220px;
    border-radius: 50%;
    background: var(--disc);
  }
  .back-mark {
    position: absolute;
    inset: 0;
    display: flex; align-items: center; justify-content: center;
    font-weight: 700;
    font-size: 96px;
  }
  .card-back--red .back-mark { color: var(--accent-red); }
  .card-back--blue .back-mark { color: var(--accent-blue); }
</style>
</head>
<body>
  <section class="card card-front--red">
    <div class="front-mark">B.R.W</div>
    <div class="front-details">
      <h1 class="business-name">B.R.W</h1>
      <p class="business-tagline">Brindlewood Auto Detailing</p>
      <address class="business-contact">
        42 Fenwarra Crs<br>
        Brindlewood Vic 3799<br>
        Ph:(03)59284736<br>
        Mob:0417362958
      </address>
    </div>
  </section>

  <section class="card card-front--slate">
    <div class="front-mark">B.R.W</div>
    <div class="front-details">
      <h1 class="business-name">B.R.W</h1>
      <p class="business-tagline">Brindlewood Auto Detailing</p>
      <address class="business-contact">
        42 Fenwarra Crs<br>
        Brindlewood Vic 3799<br>
        Ph:(03)59284736<br>
        Mob:0417362958
      </address>
    </div>
  </section>

  <section class="card card-back card-back--red">
    <div class="back-disc"></div>
    <div class="back-mark">B.R.W</div>
  </section>

  <section class="card card-back card-back--blue">
    <div class="back-disc"></div>
    <div class="back-mark">B.R.W</div>
  </section>
</body>
</html>
```